Basic Web Redesign

Hello,

We are working with a client who would like their existing website updated.

The site is http://www.lorenvasquel.com/

Currently the website is Joomla 1.0.x with Virtuemart running the small online shop.

We are extremely flexible with regards to the way forward - i.e. it can be Joomla 2.5 with Virtuemart, Wordpress plus a shopping cart, HTML 5 (no CMS) with a shopping cart or a full blown ecommerce solution using Prestashop, Magento etc.

The main constraint is a website that incorporates a working shop. At this moment the current website works, but is on extremely old versions of Joomla and Virtuemart.

So the brief is to either migrate the existing offering to a newer version of Joomla and Virtuemart OR use alternative products to achieve a very basic website with shopping cart functionality.

Reason: To enable designer to upload files and installation to be tested.

Target Market(s)

Predominantly people living on the Costa Blanca in Spain, but also some customers in the UK.

Industry/Entity Type

Shop

Requirements
Must have
• Online shop
Shipping calculator
plain badge for accepting payments
Nice to have
• Easy to use front-end for editing shop items
Easy to use front-end for editing non-shop pages

```html
<!DOCTYPE html>
<html lang="en">
<head>
<meta charset="utf-8">
<title>Loren Vasquel Floral Designer</title>
<link href="https://fonts.googleapis.com/css2?family=Arimo:wght@400;700&family=Noto+Serif:wght@400;700&display=swap" rel="stylesheet">
<style>
:root{
  --magenta:#cf0a6e;
  --magenta-dark:#a00853;
  --berry:#c2185b;
  --coral:#e8503a;
  --gold:#f7c52c;
  --gold-dark:#e6a718;
  --green:#7db536;
  --green-dark:#5e9424;
  --ink:#333333;
  --muted:#9a9a9a;
  --paper:#ffffff;
  --panel:#f5f5f5;
  --line:#e2e2e2;
}
*{margin:0;padding:0;box-sizing:border-box}
html,body{width:952px;height:1200px;overflow:hidden}
body{font-family:"Arimo",Arial,sans-serif;color:var(--ink);background:linear-gradient(180deg,var(--magenta) 0%,#c70967 60%,var(--magenta-dark) 100%);position:relative}
a{color:inherit;text-decoration:none}
.abs{position:absolute}

/* header */
.brand{left:74px;top:18px;width:150px;display:flex;align-items:center;gap:8px;color:var(--paper);font-family:"Noto Serif",Georgia,serif}
.brand-square{width:14px;height:14px;background:var(--paper);flex:none}
.brand-name{font-size:22px;line-height:1.1}
.brand-tag{left:96px;top:76px;font-family:"Noto Serif",Georgia,serif;font-size:9px;color:var(--paper);letter-spacing:.5px}
.account-links{left:396px;top:22px;display:flex;align-items:center;gap:16px;color:var(--paper);font-size:11px}
.account-links span{display:flex;align-items:center;gap:5px}
.cart{left:690px;top:14px;width:190px;height:28px;background:var(--paper);border-radius:2px;display:flex;align-items:center;gap:8px;padding-left:12px;font-size:12px;color:var(--ink)}
.cart b{color:var(--magenta)}
.order{left:416px;top:65px;color:var(--paper);font-size:17px;font-weight:700;display:flex;align-items:center;gap:6px}
.order em{font-style:normal;color:var(--gold)}
.search{left:690px;top:64px;width:190px;height:23px;background:var(--paper);border:1px solid #ddd;font-size:9px;color:var(--ink);padding:6px 10px}
.search svg{position:absolute;right:8px;top:5px}
.nav{left:397px;top:108px;width:483px;height:35px;background:linear-gradient(180deg,#fbd34a,var(--gold-dark));display:flex;border-radius:2px;box-shadow:0 2px 3px rgba(0,0,0,.2)}
.nav a{flex:1;display:flex;align-items:center;justify-content:center;font-size:12px;color:var(--ink);border-right:1px solid #d89a12}
.nav a:last-child{border-right:0}
.nav a.current{color:var(--magenta-dark)}

/* main */
.main{left:71px;top:158px;width:809px;height:960px;background:var(--paper)}
.hero{left:75px;top:163px;width:801px;height:277px;background:#e3e3e3;border-radius:4px;box-shadow:0 4px 6px rgba(0,0,0,.15)}
.hero-inner{left:82px;top:168px;width:789px;height:266px;background:linear-gradient(90deg,#ffffff 0%,#f2f2f2 60%,#e9e9e9 100%)}
.hero-photo{left:500px;top:168px;width:371px;height:266px;background:linear-gradient(120deg,#f4f4f4 0%,#dcdcdc 35%,#5f7d3c 60%,#e4a9c8 85%,#2f4a22 100%)}
.hero-title{left:116px;top:216px;font-family:"Noto Serif",Georgia,serif;font-size:22px;line-height:29px;color:var(--coral);font-weight:400}
.hero-text{left:116px;top:283px;width:350px;font-size:10.5px;line-height:18px;color:#222}
.btn-view{left:115px;top:350px;width:88px;height:27px;background:linear-gradient(180deg,#e0207e,#b8075c);color:var(--paper);font-family:"Noto Serif",Georgia,serif;font-size:11px;display:flex;align-items:center;justify-content:center;border-radius:2px;border:1px solid #fff}

.promo{top:466px;width:249px;height:123px;border-radius:2px;overflow:hidden}
.promo h2{position:absolute;left:16px;top:14px;z-index:2;font-family:"Noto Serif",Georgia,serif;font-size:19px;line-height:25px;color:var(--paper);white-space:nowrap}
.promo .read{position:absolute;left:16px;top:74px;width:101px;height:27px;background:linear-gradient(180deg,#fff,#e4e4e4);border:1px solid #ccc;font-size:9.5px;font-weight:700;color:#555;display:flex;align-items:center;justify-content:center;gap:12px}
.promo .art{position:absolute;z-index:1;border-radius:6px}
.promo-flowers{left:83px;background:linear-gradient(135deg,#c51372,#a10a58)}
.promo-flowers .art{left:145px;top:20px;width:88px;height:84px;background:linear-gradient(135deg,#f3d78c,#c99a3e)}
.promo-gifts{left:351px;background:linear-gradient(135deg,#ec6d45,#e04a3b)}
.promo-gifts .art{left:150px;top:18px;width:68px;height:92px;background:linear-gradient(135deg,#f7c437,#e0302f)}
.promo-map{left:619px;background:linear-gradient(135deg,#f5b83a,#dd8b22)}
.promo-map .art{left:140px;top:58px;width:96px;height:52px;background:linear-gradient(135deg,#e44a4a,#e8ead9)}

.section-title{left:71px;top:610px;width:809px;text-align:center;font-family:"Noto Serif",Georgia,serif;font-size:17px;color:var(--coral);font-weight:400}

.card{width:249px;height:125px;background:var(--paper);border:1px solid var(--line);box-shadow:0 2px 3px rgba(0,0,0,.08)}
.card .photo{position:absolute;left:16px;top:17px;width:98px;height:97px;border:3px solid #ececec;border-radius:4px}
.card .name{position:absolute;left:125px;top:24px;font-size:11.5px;color:var(--coral)}
.card .price{position:absolute;left:125px;top:42px;font-size:11.5px;color:var(--magenta-dark)}
.card .buy{position:absolute;left:124px;top:60px;width:105px;height:27px;background:linear-gradient(180deg,#92c446,var(--green-dark));border-radius:2px;color:var(--paper);font-family:"Noto Serif",Georgia,serif;font-size:11.5px;display:flex;align-items:center;justify-content:center;gap:8px}
.card .more{position:absolute;left:125px;top:100px;font-size:10.5px;color:var(--muted)}

.pager{left:365px;top:1080px;display:flex;gap:4px;align-items:center}
.pager span{width:18px;height:18px;background:#cfcfcf;border-radius:2px;font-size:8px;color:#888;display:flex;align-items:center;justify-content:center}
.pager span.on{background:#888;color:var(--paper)}
.pager i{font-style:normal;font-size:8px;color:#999;width:14px;text-align:center}

.footer-links{left:71px;top:1139px;display:flex;gap:8px;font-size:11.5px;color:var(--paper)}
.copy{left:71px;top:1166px;font-size:11.5px;color:var(--paper)}
.payments{left:665px;top:1147px;display:flex;gap:8px}
.payments span{width:24px;height:16px;background:#f1f1f1;border-radius:2px}
.social{left:827px;top:1146px;display:flex;gap:7px}
.social span{width:24px;height:24px;border-radius:50%;background:var(--paper)}
</style>
</head>
<body>

<header>
  <div class="abs brand"><span class="brand-square"></span><span class="brand-name">Loren Vasquel</span></div>
  <div class="abs brand-tag">FLORAL DESIGNER</div>

  <nav class="abs account-links">
    <span><svg width="14" height="14" viewBox="0 0 14 14"><circle cx="7" cy="4" r="3.5" fill="#fff"/><path d="M0 14c0-5 14-5 14 0z" fill="#fff"/></svg>My Account</span><span>|</span>
    <span><svg width="14" height="14" viewBox="0 0 14 14"><rect x="1" y="2" width="11" height="11" fill="none" stroke="#fff" stroke-width="1.5"/><path d="M3 7l3 3 7-9" fill="none" stroke="#fff" stroke-width="2"/></svg>Check Out</span><span>|</span>
    <span><svg width="12" height="14" viewBox="0 0 12 14"><path d="M3 6V4a3 3 0 016 0v2" fill="none" stroke="#fff" stroke-width="1.5"/><rect x="1" y="6" width="10" height="8" fill="#fff"/></svg>Logout</span>
  </nav>

  <div class="abs cart"><svg width="20" height="16" viewBox="0 0 20 16"><path d="M1 1h3l2 10h11l2-7H5" fill="none" stroke="#c2185b" stroke-width="1.4"/><circle cx="8" cy="14" r="1.5" fill="#c2185b"/><circle cx="15" cy="14" r="1.5" fill="#c2185b"/></svg><span><b>0</b> item(s) &nbsp;/&nbsp; Total : <b>$0.00</b></span></div>

  <div class="abs order"><svg width="14" height="14" viewBox="0 0 14 14"><path d="M3 1l3 3-2 2c1 2 2 3 4 4l2-2 3 3-2 2C6 13 1 8 1 3z" fill="#fff"/></svg>Order Now : <em>0034 96 555 0187</em></div>
  <div class="abs search">Search<svg width="13" height="13" viewBox="0 0 13 13"><circle cx="5" cy="5" r="4" fill="none" stroke="#999" stroke-width="1.6"/><path d="M8 8l4 4" stroke="#999" stroke-width="2"/></svg></div>

  <nav class="abs nav">
    <a class="current" href="#">Home</a><a href="#">About</a><a href="#">Delivery</a><a href="#">Gift Ideas</a><a href="#">Gallery</a><a href="#">Contact</a>
  </nav>
</header>

<main>
  <div class="abs main"></div>
  <div class="abs hero"></div>
  <div class="abs hero-inner"></div>
  <div class="abs hero-photo" role="img" aria-label="Bride and groom holding hands over a pink and white wedding bouquet"></div>
  <h1 class="abs hero-title">Welcome to Loren Vasquel Designs,<br>our aim is to inspire!</h1>
  <p class="abs hero-text">We offer beautiful flowers and plants for all tastes and budgets, and whats more, we will deliver them to your loved ones, a service that is not often found in this area of the Costa Blanca, Spain.</p>
  <a class="abs btn-view" href="#">VIEW MORE</a>

  <section class="abs promo promo-flowers"><h2>Flowers<br>for Delivery</h2><a class="read" href="#">READ MORE <svg width="5" height="7"><path d="M0 0l5 3.5L0 7z" fill="#555"/></svg></a><div class="art" role="img" aria-label="Cardboard delivery box"></div></section>
  <section class="abs promo promo-gifts"><h2>Gifts and<br>Ideas</h2><a class="read" href="#">READ MORE <svg width="5" height="7"><path d="M0 0l5 3.5L0 7z" fill="#555"/></svg></a><div class="art" role="img" aria-label="Wrapped gift box with red ribbon"></div></section>
  <section class="abs promo promo-map"><h2>Map of Delivery<br>Areas</h2><a class="read" href="#">READ MORE <svg width="5" height="7"><path d="M0 0l5 3.5L0 7z" fill="#555"/></svg></a><div class="art" role="img" aria-label="Folded map with location pin"></div></section>

  <h2 class="abs section-title">Our Flowers</h2>

  <div class="abs card" style="left:83px;top:641px"><div class="photo" role="img" aria-label="Table centrepiece at a reception" style="background:linear-gradient(135deg,#7a4a36,#e9d8d2)"></div><div class="name">Product Name</div><div class="price">Price : $00.00</div><a class="buy" href="#"><svg width="16" height="13" viewBox="0 0 16 13"><path d="M1 1h2l2 8h8l2-6H4" fill="none" stroke="#fff" stroke-width="1.5"/><circle cx="6" cy="11.5" r="1.2" fill="#fff"/><circle cx="12" cy="11.5" r="1.2" fill="#fff"/></svg>BUY NOW</a><div class="more">VIEW MORE</div></div>
  <div class="abs card" style="left:351px;top:641px"><div class="photo" role="img" aria-label="White calla lily bouquet" style="background:linear-gradient(135deg,#f4f4ee,#b9c6a6)"></div><div class="name">Product Name</div><div class="price">Price : $00.00</div><a class="buy" href="#"><svg width="16" height="13" viewBox="0 0 16 13"><path d="M1 1h2l2 8h8l2-6H4" fill="none" stroke="#fff" stroke-width="1.5"/><circle cx="6" cy="11.5" r="1.2" fill="#fff"/><circle cx="12" cy="11.5" r="1.2" fill="#fff"/></svg>BUY NOW</a><div class="more">VIEW MORE</div></div>
  <div class="abs card" style="left:619px;top:641px"><div class="photo" role="img" aria-label="Pink rose bouquet" style="background:linear-gradient(135deg,#f0a0a8,#6f9a5a)"></div><div class="name">Product Name</div><div class="price">Price : $00.00</div><a class="buy" href="#"><svg width="16" height="13" viewBox="0 0 16 13"><path d="M1 1h2l2 8h8l2-6H4" fill="none" stroke="#fff" stroke-width="1.5"/><circle cx="6" cy="11.5" r="1.2" fill="#fff"/><circle cx="12" cy="11.5" r="1.2" fill="#fff"/></svg>BUY NOW</a><div class="more">VIEW MORE</div></div>

  <div class="abs card" style="left:83px;top:783px"><div class="photo" role="img" aria-label="White roses in a glass vase" style="background:linear-gradient(135deg,#e9eae2,#8f9a86)"></div><div class="name">Product Name</div><div class="price">Price : $00.00</div><a class="buy" href="#"><svg width="16" height="13" viewBox="0 0 16 13"><path d="M1 1h2l2 8h8l2-6H4" fill="none" stroke="#fff" stroke-width="1.5"/><circle cx="6" cy="11.5" r="1.2" fill="#fff"/><circle cx="12" cy="11.5" r="1.2" fill="#fff"/></svg>BUY NOW</a><div class="more">VIEW MORE</div></div>
  <div class="abs card" style="left:351px;top:783px"><div class="photo" role="img" aria-label="Red and purple orchid bouquet" style="background:linear-gradient(135deg,#d0305a,#7a2a6a)"></div><div class="name">Product Name</div><div class="price">Price : $00.00</div><a class="buy" href="#"><svg width="16" height="13" viewBox="0 0 16 13"><path d="M1 1h2l2 8h8l2-6H4" fill="none" stroke="#fff" stroke-width="1.5"/><circle cx="6" cy="11.5" r="1.2" fill="#fff"/><circle cx="12" cy="11.5" r="1.2" fill="#fff"/></svg>BUY NOW</a><div class="more">VIEW MORE</div></div>
  <div class="abs card" style="left:619px;top:783px"><div class="photo" role="img" aria-label="White flower bouquet on a dark background" style="background:radial-gradient(circle,#f2f2f2 0%,#5e6a5a 55%,#111 100%)"></div><div class="name">Product Name</div><div class="price">Price : $00.00</div><a class="buy" href="#"><svg width="16" height="13" viewBox="0 0 16 13"><path d="M1 1h2l2 8h8l2-6H4" fill="none" stroke="#fff" stroke-width="1.5"/><circle cx="6" cy="11.5" r="1.2" fill="#fff"/><circle cx="12" cy="11.5" r="1.2" fill="#fff"/></svg>BUY NOW</a><div class="more">VIEW MORE</div></div>

  <div class="abs card" style="left:83px;top:933px"><div class="photo" role="img" aria-label="White daisy bouquet with pink ribbon" style="background:linear-gradient(135deg,#f6f6f0,#e63a95)"></div><div class="name">Product Name</div><div class="price">Price : $00.00</div><a class="buy" href="#"><svg width="16" height="13" viewBox="0 0 16 13"><path d="M1 1h2l2 8h8l2-6H4" fill="none" stroke="#fff" stroke-width="1.5"/><circle cx="6" cy="11.5" r="1.2" fill="#fff"/><circle cx="12" cy="11.5" r="1.2" fill="#fff"/></svg>BUY NOW</a><div class="more">VIEW MORE</div></div>
  <div class="abs card" style="left:351px;top:933px"><div class="photo" role="img" aria-label="Tiered wedding cake with flowers" style="background:linear-gradient(135deg,#3a2418,#e7c9a2)"></div><div class="name">Product Name</div><div class="price">Price : $00.00</div><a class="buy" href="#"><svg width="16" height="13" viewBox="0 0 16 13"><path d="M1 1h2l2 8h8l2-6H4" fill="none" stroke="#fff" stroke-width="1.5"/><circle cx="6" cy="11.5" r="1.2" fill="#fff"/><circle cx="12" cy="11.5" r="1.2" fill="#fff"/></svg>BUY NOW</a><div class="more">VIEW MORE</div></div>
  <div class="abs card" style="left:619px;top:933px"><div class="photo" role="img" aria-label="Cream rose bridal bouquet" style="background:linear-gradient(135deg,#f7f3e4,#b9b29a)"></div><div class="name">Product Name</div><div class="price">Price : $00.00</div><a class="buy" href="#"><svg width="16" height="13" viewBox="0 0 16 13"><path d="M1 1h2l2 8h8l2-6H4" fill="none" stroke="#fff" stroke-width="1.5"/><circle cx="6" cy="11.5" r="1.2" fill="#fff"/><circle cx="12" cy="11.5" r="1.2" fill="#fff"/></svg>BUY NOW</a><div class="more">VIEW MORE</div></div>

  <nav class="abs pager"><span class="on">1</span><span>2</span><span>3</span><span>4</span><span>5</span><span>6</span><span>7</span><span>8</span><span>»</span><i>...</i><span>»»</span></nav>
</main>

<footer>
  <nav class="abs footer-links"><a href="#">Home</a>|<a href="#">About</a>|<a href="#">Delivery</a>|<a href="#">Gift Ideas</a>|<a href="#">Gallery</a>|<a href="#">Contact</a>|<a href="#">Partners</a>|<a href="#">Links</a>|<a href="#">My Account</a></nav>
  <p class="abs copy">Copyright &copy; Loren Vasquel. &nbsp; All rights reserved.</p>
  <div class="abs payments" aria-label="Accepted payment methods"><span></span><span></span><span></span><span></span><span></span></div>
  <div class="abs social" aria-label="Social networks"><span></span><span></span></div>
</footer>

</body>
</html>
```